Kestrel Fitness Studio Retail Tube Design

We require a design for cardboard tubes, like images included, which will be the main packaging for the clothing sold in our fitness studio. Kestrel Fitness Studio is an upscale customer service driven fitness studio that is geared towards improving our clients/members quality of life by marrying cutting edge technology like 3D scanning and metabolic measurement with first class training based on 30+ years of experience in the industry.

The project will require a design which revolves around the tube seamlessly including the lid and its top and must include the company logo, which is included, along with our web address (www.kestrelgymhall.example).

The final design should be a bold, sleek design which stands out so when people see the tube they will either know it’s from our studio or be curious as to want company it’s from. Similar to the impact the Moravanti bag has that is given to all their customers.

Target Market(s)

Individuals and groups seeking individualize fitness programs which produce results.

Industry/Entity Type

Clothing

Colors

Designer to choose colors to be used in the design.

Requirements
Must have
• Logo and website address

```html
<!DOCTYPE html>
<html lang="en">
<head>
<meta charset="utf-8">
<title>Kestrel Fitness Studio – Retail Tube Wrap</title>
<link rel="stylesheet" href="https://fonts.googleapis.com/css2?family=Josefin+Sans:wght@300&display=swap">
<style>
  :root {
    --bg-top: #f4f4f4;
    --bg-bottom: #c9c9c9;
    --paper: #ffffff;
    --ink: #0b0b0b;
    --red: #d0032f;
    --red-deep: #b00020;
    --seam: #9a9a9a;
    --lid: #111111;
    --lid-text: #f2f2f2;
  }
  * { box-sizing: border-box; margin: 0; padding: 0; }
  html, body { width: 1200px; height: 1200px; overflow: hidden; }
  body {
    position: relative;
    background: linear-gradient(180deg, var(--bg-top), var(--bg-bottom));
    font-family: "Josefin Sans", "Helvetica Neue", Arial, sans-serif;
    font-weight: 300;
  }

  /* Lid top */
  .lid-top {
    position: absolute;
    left: 70px; top: 480px;
    width: 250px; height: 250px;
    border-radius: 50%;
    background: var(--lid);
    display: flex; flex-direction: column;
    align-items: center; justify-content: center;
    color: var(--lid-text);
    text-align: center;
  }
  .lid-top__name {
    font-size: 17px;
    letter-spacing: 3px;
    text-transform: uppercase;
    line-height: 1.4;
  }

  /* Unrolled wrap */
  .tube-wrap {
    position: absolute;
    left: 400px; top: 220px;
    width: 740px; height: 760px;
    background: var(--paper);
    overflow: hidden;
  }
  .lid-band {
    position: absolute;
    left: 0; right: 0; top: 0;
    height: 110px;
    background: linear-gradient(90deg, var(--ink), var(--red) 50%, var(--ink));
  }
  .lid-seam {
    position: absolute;
    left: 0; right: 0; top: 139px;
    height: 2px;
    background: var(--seam);
  }
  .base-band {
    position: absolute;
    left: 0; right: 0; bottom: 0;
    height: 210px;
    background: linear-gradient(90deg, var(--ink), var(--red-deep) 50%, var(--ink));
  }
  .brand {
    position: absolute;
    left: 0; right: 0; top: 360px;
    text-align: center;
  }
  .brand__name {
    display: inline-flex; align-items: center; gap: 16px;
    font-size: 40px;
    letter-spacing: 5px;
    text-transform: uppercase;
    color: var(--ink);
  }
  .brand__mark {
    width: 22px; height: 22px;
    background: var(--red);
  }
  .brand__web {
    margin-top: 18px;
    font-size: 19px;
    letter-spacing: 2px;
    color: var(--red);
  }
</style>
</head>
<body>

  <div class="lid-top">
    <div class="lid-top__name">Kestrel<br>Fitness Studio</div>
  </div>

  <div class="tube-wrap">
    <div class="lid-band" role="img" aria-label="Decorative band of hanging red and black bars around the lid"></div>
    <div class="lid-seam"></div>

    <div class="brand">
      <div class="brand__name"><span class="brand__mark"></span>Kestrel Fitness Studio</div>
      <div class="brand__web">www.kestrelgymhall.example</div>
    </div>

    <div class="base-band" role="img" aria-label="Decorative band of rising red and black bars around the base"></div>
  </div>

</body>
</html>
```